Design Our Holiday Magic Coupon

Purpose - The purpose of this project is to create a festive, uplifting, and visually engaging physical coupon that will be mailed to our existing community and warm leads.
The intent is twofold: first, to spark delight and connection by offering a tangible, personal touch during the holiday season; and second, to encourage customers to explore and purchase our programs as they prepare for a strong start to 2026. This mailer is designed to re-engage past buyers, inspire current participants, and gently invite new momentum into their practice through a simple, friendly offer.

Project Description + Scope

This project includes the design and production of a printed coupon ( card format) featuring a 20% discount on purchases of $79 or more. The copy should feel warm, clear, and celebratory without urgency or pressure.

The front of the card will include the headline (“Live Your Best 2026”), bold discount information, and the coupon code FESTIVE20. The back will include a short message reinforcing the tone of possibility and ease, plus simple redemption instructions and the expiry date: December 31, 2025. Deliverables include print-ready artwork, color selection aligned with KH brand style.

one side
LIVE YOUR BEST 2026
Enjoy 20% OFF when you buy $79 or more.
Use code: FESTIVE20
Redeem until end of day December 31, 2025.

Back side - Move with clarity.
Heal with intelligence.
Lead with ease.
Thank you for being part of Kinetic Harmony.
Lots of love, Mara and the whole of Team Mara

Target Market(s)

yoga teachers, yoga lovers, mostly over 50 years, women

Font styles to use
Other font styles liked:
• see attached for feel

Colors
0054AA
0677BA
7BADD7
CADEEF
E8F1F8
0094D4
00A9DD
6FCCEA
C7EBF8
E9F6FB
00AB8E
00BBA5
67D7C9
C6EFE9
E9F9F6
EB3D1F
EC4F4E
F09395
F8D3D4
FCEDEE

Requirements
Nice to have
• see attached

```html
<!DOCTYPE html>
<html lang="en">
<head>
<meta charset="utf-8">
<title>Kinetic Harmony – Holiday Coupon</title>
<link rel="stylesheet" href="https://fonts.googleapis.com/css2?family=Noto+Serif:wght@400;500&family=Poppins:wght@400&display=swap">
<style>
  :root {
    --page-bg: #e4e4e4;
    --card-deep: #45278e;
    --card-mid: #4a63b1;
    --card-light: #5da3d2;
    --ink: #ffffff;
    --ink-soft: rgba(255,255,255,0.92);
    --badge-fill: rgba(123,173,215,0.55);
    --code-fill: rgba(123,173,215,0.35);
  }
  * { margin: 0; padding: 0; box-sizing: border-box; }
  html, body { width: 871px; height: 1200px; overflow: hidden; }
  body { background: var(--page-bg); position: relative; font-family: "Poppins", sans-serif; color: var(--ink); }

  .card {
    position: absolute; left: 155px; width: 562px; height: 378px;
    border-radius: 26px; overflow: hidden;
  }
  .card--front { top: 160px; }
  .card--back { top: 662px; }

  .card__sky {
    position: absolute; inset: 0;
    background: linear-gradient(32deg, var(--card-deep) 0%, var(--card-mid) 45%, var(--card-light) 100%);
  }
  .card__content { position: absolute; inset: 0; }
  .line { position: absolute; left: 0; right: 0; text-align: center; }

  .brand { top: 34px; display: flex; flex-direction: column; align-items: center; gap: 5px; }
  .brand__dot { width: 20px; height: 20px; border-radius: 50%; background: var(--ink); }
  .brand__name { font-family: "Noto Serif", serif; font-size: 13px; font-weight: 400; color: var(--ink); line-height: 1; }

  .headline {
    top: 118px; font-family: "Noto Serif", serif; font-weight: 500;
    font-size: 43px; letter-spacing: -0.3px; line-height: 1.2;
    text-shadow: 0 0 10px rgba(255,255,255,0.45);
  }
  .offer { top: 206px; display: flex; justify-content: center; align-items: center; gap: 8px; font-family: "Noto Serif", serif; }
  .offer__lead { font-size: 24px; padding-top: 4px; }
  .offer__badge {
    font-size: 37px; font-weight: 500; line-height: 1; padding: 4px 8px 3px;
    border: 2px solid var(--ink); background: var(--badge-fill);
  }
  .condition { top: 262px; font-size: 13.5px; }
  .code { top: 291px; display: flex; justify-content: center; }
  .code__box { border: 2px solid var(--ink); background: var(--code-fill); font-size: 16.5px; padding: 3px 12px; line-height: 1.3; }
  .expiry { top: 337px; font-size: 13.5px; }

  .motto {
    top: 112px; font-family: "Noto Serif", serif; font-size: 35px; line-height: 47px; font-weight: 400;
  }
  .signature { top: 271px; font-size: 15.5px; }
  .thanks { top: 303px; font-size: 14.5px; line-height: 23px; color: var(--ink-soft); }
</style>
</head>
<body>

<section class="card card--front" aria-label="Coupon front">
  <div class="card__sky" role="img" aria-label="Starry night sky in deep violet to soft blue with faint floral swirls"></div>
  <div class="card__content">
    <div class="line brand"><span class="brand__dot"></span><span class="brand__name">kinetic harmony</span></div>
    <h1 class="line headline">LIVE YOUR BEST 2026</h1>
    <p class="line offer"><span class="offer__lead">Enjoy</span><span class="offer__badge">20% OFF</span></p>
    <p class="line condition">when you buy $79 or more.</p>
    <p class="line code"><span class="code__box">Use code: FESTIVE20</span></p>
    <p class="line expiry">Redeem until end of day December 31, 2025.</p>
  </div>
</section>

<section class="card card--back" aria-label="Coupon back">
  <div class="card__sky" role="img" aria-label="Starry night sky in deep violet to soft blue with faint floral swirls"></div>
  <div class="card__content">
    <div class="line brand"><span class="brand__dot"></span><span class="brand__name">kinetic harmony</span></div>
    <p class="line motto">Move with clarity.<br>Heal with intelligence.<br>Lead with ease.</p>
    <p class="line signature">- Mara Ellison -</p>
    <p class="line thanks">Thank you for being part of Kinetic Harmony.<br>Lots of love, Mara and the whole of Team Mara</p>
  </div>
</section>

</body>
</html>
```